Business cards for law firm with global theme

I'd like business cards with contact info for two offices. They should include the colors and font of the new logo design, which is a stylized globe with an "F" in it. The feel should be very modern and professional.

```html
<!DOCTYPE html>
<html lang="en">
<head>
<meta charset="utf-8">
<title>Marovena Law – Business Card</title>
<link href="https://fonts.googleapis.com/css2?family=Montserrat:wght@400;500;600;700;800&display=swap" rel="stylesheet">
<style>
  :root {
    --backdrop: #2c2d30;
    --navy: #1f3f6e;
    --navy-deep: #15305a;
    --sky: #29a8e0;
    --text-grey: #4a4f58;
    --rule: #9fc7e4;
    --card-white: #ffffff;
  }
  * { margin: 0; padding: 0; box-sizing: border-box; }
  html, body {
    width: 1200px;
    height: 1186px;
    overflow: hidden;
    background: var(--backdrop);
    font-family: "Montserrat", sans-serif;
  }
  .canvas { position: relative; width: 1200px; height: 1186px; }
  .card {
    position: absolute;
    width: 760px;
    height: 434px;
    border-radius: 30px;
    overflow: hidden;
    box-shadow: 0 18px 40px rgba(0,0,0,0.45);
  }
  .card-back { left: 90px; top: 90px; }
  .back-pattern {
    position: absolute;
    inset: 0;
    background: linear-gradient(135deg, #5a8fc0 0%, #2f5f96 40%, var(--navy-deep) 100%);
  }
  .back-mark {
    position: absolute;
    right: 60px;
    top: 200px;
    width: 56px;
    height: 56px;
    border-radius: 50%;
    background: var(--sky);
  }
  .card-front { left: 350px; top: 650px; background: var(--card-white); }
  .brand-mark {
    position: absolute;
    left: 60px;
    top: 100px;
    width: 190px;
    height: 180px;
    border-radius: 50%;
    background: linear-gradient(135deg, var(--sky) 0%, #2f6fae 55%, var(--navy) 100%);
  }
  .wordmark {
    position: absolute;
    left: 290px;
    top: 78px;
    width: 420px;
    color: var(--navy);
    font-weight: 800;
    text-transform: uppercase;
  }
  .wordmark-main {
    display: block;
    font-size: 54px;
    line-height: 1;
    letter-spacing: 1px;
    text-align: center;
  }
  .wordmark-sub {
    display: flex;
    align-items: center;
    gap: 16px;
    margin-top: 10px;
    font-size: 32px;
    line-height: 1;
    letter-spacing: 2px;
  }
  .wordmark-sub::before,
  .wordmark-sub::after {
    content: "";
    flex: 1;
    height: 2px;
    background: var(--sky);
  }
  .person {
    position: absolute;
    left: 60px;
    top: 300px;
    width: 310px;
    text-align: right;
  }
  .person-name { font-weight: 700; font-size: 30px; color: var(--sky); }
  .person-title { font-weight: 400; font-size: 17px; color: var(--text-grey); margin-top: 4px; }
  .divider {
    position: absolute;
    left: 392px;
    top: 250px;
    width: 1px;
    height: 100px;
    background: var(--rule);
  }
  .contact { position: absolute; left: 420px; top: 252px; list-style: none; }
  .contact li {
    display: flex;
    align-items: center;
    gap: 14px;
    font-size: 18px;
    color: var(--text-grey);
    height: 32px;
  }
  .contact svg { width: 16px; height: 16px; flex: none; }
</style>
</head>
<body>
<main class="canvas">
  <section class="card card-back">
    <div class="back-pattern" role="img" aria-label="Card back: repeating embossed brand-mark pattern on deep blue"></div>
    <span class="back-mark"></span>
  </section>

  <section class="card card-front">
    <span class="brand-mark"></span>
    <div class="wordmark">
      <span class="wordmark-main">Marovena</span>
      <span class="wordmark-sub">Law</span>
    </div>

    <div class="person">
      <p class="person-name">Daniel Brooks</p>
      <p class="person-title">CEO &amp; Founder</p>
    </div>

    <div class="divider"></div>

    <ul class="contact">
      <li>
        <svg viewBox="0 0 16 16" aria-hidden="true"><path fill="#1f3f6e" d="M3.5 1.5l2.5 3-1.5 1.6c.8 1.8 2.2 3.2 4 4l1.6-1.5 3 2.5-1.4 2.4C6.6 13.3 2.7 9.4 1.1 2.9z"/></svg>
        (555) 014-2278
      </li>
      <li>
        <svg viewBox="0 0 16 16" aria-hidden="true"><rect x="1" y="3" width="14" height="10" rx="1.5" fill="#1f3f6e"/><path d="M1.5 4l6.5 5 6.5-5" stroke="#fff" stroke-width="1.4" fill="none"/></svg>
        info@marovenalaw.com
      </li>
      <li>
        <svg viewBox="0 0 16 16" aria-hidden="true"><circle cx="8" cy="8" r="7" fill="#1f3f6e"/><path d="M1 8h14M8 1c-2.5 2.6-2.5 11.4 0 14M8 1c2.5 2.6 2.5 11.4 0 14" stroke="#fff" stroke-width="1" fill="none"/></svg>
        www.marovenalaw.com
      </li>
    </ul>
  </section>
</main>
</body>
</html>
```